New business card for UK roofing company

We are Brindmore Roofing and we need a business card design for our staff.

We offer the following services:

- New roofs
- General roof repairs
- Drone surveys
- Single ply roofing
- Steel cladding
- Asbestos removal
- Electronic leak detection

I have attached our logo. I have also attached example branding printed to our vans. The business card should fit in with the style of our branding.

The business card should have the following information;

Address:
Unit 17c Wendlecroft Farm
Wendlecroft Lane
Hatchington
CM4 9QD

Telephone: 020 7946 0372
24 Hour: 0800 612 4479

Email: ray@brindmoreroofing.example
Mobile: 07700981234
Name: Ray Tunstead
Website: www.brindmoreroofing.example

The business card will be printed in Spot UV, see here: https://www.kestaprint.example/business-cards/spot-uv/

If you need anymore info, please let me know,

```html
<!DOCTYPE html>
<html lang="en">
<head>
<meta charset="utf-8">
<title>Brindmore Roofing – Business Card</title>
<link rel="stylesheet" href="https://fonts.googleapis.com/css2?family=Poppins:wght@600;700&family=Roboto:wght@400&display=swap">
<style>
  :root {
    --stage: #2a2a2a;
    --brand-blue: #1ea2d2;
    --brand-navy: #1d3e6c;
    --card-white: #ececec;
    --ink: #2b2b2b;
  }
  * { margin: 0; padding: 0; box-sizing: border-box; }
  html, body { width: 1200px; height: 1138px; overflow: hidden; background: var(--stage); }
  .stage { position: relative; width: 1200px; height: 1138px; }

  .card {
    position: absolute;
    width: 620px;
    height: 376px;
    border-radius: 16px;
    overflow: hidden;
  }
  .card--front { left: 272px; top: 184px; background: var(--brand-blue); }
  .card--back { left: 274px; top: 606px; background: var(--card-white); }

  .front-brand {
    position: absolute;
    left: 0; right: 0; top: 138px;
    text-align: center;
  }
  .front-brand__name {
    font-family: "Poppins", sans-serif;
    font-weight: 700;
    font-size: 48px;
    line-height: 1;
    letter-spacing: -1px;
    color: #ffffff;
  }
  .front-brand__tagline {
    margin-top: 14px;
    font-family: "Poppins", sans-serif;
    font-weight: 600;
    font-size: 13px;
    letter-spacing: 1.6px;
    color: var(--brand-navy);
  }

  .back-brand {
    position: absolute;
    left: 0; width: 338px; top: 102px;
    text-align: center;
  }
  .back-brand__mark { display: block; margin: 0 auto 18px; }
  .back-brand__name {
    font-family: "Poppins", sans-serif;
    font-weight: 700;
    font-size: 29px;
    line-height: 1;
    letter-spacing: -0.5px;
    color: var(--brand-navy);
  }

  .divider {
    position: absolute;
    left: 338px; top: 52px;
    width: 1.5px; height: 272px;
    background: var(--brand-blue);
  }

  .contact {
    position: absolute;
    left: 374px; top: 60px;
    font-family: "Roboto", sans-serif;
    color: var(--ink);
  }
  .contact__name {
    font-family: "Poppins", sans-serif;
    font-weight: 600;
    font-size: 25px;
    line-height: 1.2;
    color: var(--brand-navy);
    margin-bottom: 8px;
  }
  .contact__row {
    display: flex; align-items: center;
    font-size: 14.5px; line-height: 24px;
  }
  .contact__row svg { width: 14px; height: 14px; margin-right: 13px; flex: none; }
  .contact__address { margin-top: 16px; font-size: 16px; line-height: 24px; }
  .contact__lines { margin-top: 10px; font-size: 16px; line-height: 24px; }
  .contact__label { color: var(--brand-blue); }
</style>
</head>
<body>
<main class="stage">

  <section class="card card--front" aria-label="Card front">
    <div class="front-brand">
      <div class="front-brand__name">Brindmore Roofing</div>
      <div class="front-brand__tagline">COMMERCIAL &amp; RESIDENTIAL ROOFING SERVICES</div>
    </div>
  </section>

  <section class="card card--back" aria-label="Card back">
    <div class="back-brand">
      <svg class="back-brand__mark" width="80" height="80" viewBox="0 0 80 80" aria-hidden="true">
        <circle cx="40" cy="40" r="38" fill="var(--brand-blue)"/>
      </svg>
      <div class="back-brand__name">Brindmore Roofing</div>
    </div>

    <div class="divider"></div>

    <div class="contact">
      <div class="contact__name">Ray Tunstead</div>
      <div class="contact__row">
        <svg viewBox="0 0 16 16" aria-hidden="true"><path fill="var(--brand-blue)" d="M1 6c0-2 3-3 7-3s7 1 7 3v1h-4V5.5H5V7H1zM3 8h10l1 6H2z"/></svg>
        07700981234
      </div>
      <div class="contact__row">
        <svg viewBox="0 0 16 16" aria-hidden="true"><rect x="1" y="3" width="14" height="10" fill="var(--brand-blue)"/><path d="M1 3l7 6 7-6" fill="none" stroke="#fff" stroke-width="1.3"/></svg>
        ray@brindmoreroofing.example
      </div>
      <div class="contact__row">
        <svg viewBox="0 0 16 16" aria-hidden="true"><g fill="none" stroke="var(--brand-blue)" stroke-width="1.3"><circle cx="8" cy="8" r="6.5"/><ellipse cx="8" cy="8" rx="3" ry="6.5"/><path d="M1.5 8h13M2.5 4.5h11M2.5 11.5h11"/></g></svg>
        www.brindmoreroofing.example
      </div>
      <div class="contact__address">
        Unit 17c Wendlecroft Farm<br>
        Wendlecroft Lane<br>
        Hatchington CM4 9QD
      </div>
      <div class="contact__lines">
        <div><span class="contact__label">Telephone:</span> 020 7946 0372</div>
        <div><span class="contact__label">24 Hour:</span> 0800 612 4479</div>
      </div>
    </div>
  </section>

</main>
</body>
</html>
```